Business Card Design/Stationary Design

We would like designers to submit cool, hip business card designs (plus stationary designs) for a new, upstart software development company located in Toronto.
If you have any questions, please email us.
For inspiration on designs:
http://cardmuse.example/cool-business-cards/
http://layoutnotes.example/2008/05/36-cool-business-cards-you-should%E2%80%99ve-seen.html
http://gigharbor.example/general/18-smokin-hot-business-card-designs/

Card info:

Selvakumar (Selv) Nadarasan

Founder and CEO

47 Brindle Court, Suite 311

Toronto, ON M4K 2T8

Phone: 647-512-7730

Mobile: 416-273-5094

Fax: 647-512-7731

Email: selvakumar.nadarasan@mailbrook.example

www.quendrix.example
Updates

Hi everyone,

In terms of all the designs I have seen so far, here is what I like:

1.  I really like the "back" part of this design.  The "front" looks pretty decent as well, but for the "front", look at #2 on this list.  I like that.

http://www.pitchboard.example/image.aspx?imageLocation=1000_10001_2000_image.jpg&type=design300px&whiteLabelCustId=9999

2. "Side 1" of this I like, the front needs to be reworked.

http://www.pitchboard.example/image.aspx?imageLocation=1000_10002_2000_image.png&type=design300px&whiteLabelCustId=9999

3. http://www.pitchboard.example/image.aspx?imageLocation=1000_10003_2000_image.jpg&type=design300px&whiteLabelCustId=9999

4. http://www.pitchboard.example/image.aspx?imageLocation=1000_10004_2000_image.jpg&type=design300px&whiteLabelCustId=9999

Target Market(s)

We are focused on enterprise customers right now, so businesses with a long-term goal of also reaching out to the consumer market as well.

Industry/Entity Type

Software

Requirements
Must have
• Must look cool, ultra-modern, clean and eye-catching. Must incorporate our logo and the colors found in the logo.

```html
<!DOCTYPE html>
<html lang="en">
<head>
<meta charset="utf-8">
<title>Quendrix Business Cards</title>
<link rel="stylesheet" href="https://fonts.googleapis.com/css2?family=Jost:ital,wght@0,400;0,500;0,600;1,600&family=Source+Sans+3:ital,wght@0,400;1,400&display=swap">
<style>
  :root {
    --stage: #4e8a05;
    --brand-green: #4e8a05;
    --lime: #c9f200;
    --logo-green: #8cc63f;
    --ink: #111111;
    --paper: #ffffff;
    --shadow: rgba(0,0,0,0.55);
  }
  * { margin: 0; padding: 0; box-sizing: border-box; }
  html, body { width: 1200px; height: 955px; overflow: hidden; background: var(--paper); }
  .stage {
    position: absolute; left: 19px; top: 19px; width: 1131px; height: 885px;
    background: var(--stage);
    box-shadow: 14px 14px 18px var(--shadow);
  }
  .card {
    position: absolute; width: 600px; height: 343px;
    background: var(--paper);
    border: 2px solid var(--ink);
    box-shadow: 14px 14px 14px var(--shadow);
    overflow: hidden;
  }
  .card-front { left: 51px; top: 117px; }
  .card-back { left: 477px; top: 419px; }

  .brand { position: absolute; display: flex; align-items: center; }
  .brand-dot { border-radius: 50%; background: var(--logo-green); flex: none; }
  .brand-name { font-family: "Jost", sans-serif; font-weight: 400; color: var(--ink); line-height: 1; }

  .card-front .brand { left: 50px; top: 95px; gap: 40px; }
  .card-front .brand-dot { width: 128px; height: 128px; }
  .card-front .brand-name { font-size: 74px; letter-spacing: 1px; }

  .holder {
    position: absolute; left: 18px; right: 26px; top: 20px; height: 72px;
    display: flex; align-items: baseline; justify-content: space-between; gap: 16px;
    white-space: nowrap;
  }
  .holder-name {
    font-family: "Source Sans 3", sans-serif; font-weight: 400;
    font-size: 54px; line-height: 1; color: var(--brand-green); letter-spacing: -1px;
  }
  .holder-title {
    font-family: "Source Sans 3", sans-serif; font-style: italic;
    font-size: 21px; color: var(--brand-green);
  }
  .info-band {
    position: absolute; left: 0; right: 0; top: 97px; height: 164px;
    background: var(--lime);
    border-top: 5px solid var(--brand-green);
    border-bottom: 5px solid var(--brand-green);
    font-family: "Jost", sans-serif; color: var(--ink);
  }
  .address {
    position: absolute; left: 28px; top: 30px;
    font-weight: 600; font-size: 24px; line-height: 31px;
  }
  .phones {
    position: absolute; right: 22px; top: 32px;
    font-weight: 600; font-size: 25px; line-height: 31px; letter-spacing: 0.5px;
  }
  .phones .label { font-size: 16px; font-weight: 500; margin-left: 6px; }
  .email {
    position: absolute; right: 28px; top: 104px;
    font-weight: 500; font-size: 20px; letter-spacing: 1px;
  }
  .website {
    position: absolute; left: 31px; top: 290px;
    font-family: "Jost", sans-serif; font-style: italic; font-weight: 600;
    font-size: 24px; letter-spacing: 2.5px; color: var(--brand-green);
  }
  .card-back .brand { right: 24px; top: 281px; gap: 10px; }
  .card-back .brand-dot { width: 38px; height: 38px; }
  .card-back .brand-name { font-size: 22px; }
</style>
</head>
<body>
  <div class="stage">
    <section class="card card-front" aria-label="Card front">
      <div class="brand">
        <span class="brand-dot"></span>
        <span class="brand-name">Quendrix</span>
      </div>
    </section>

    <section class="card card-back" aria-label="Card back">
      <header class="holder">
        <h1 class="holder-name">Selv Nadarasan</h1>
        <p class="holder-title">Technology Consultant</p>
      </header>
      <div class="info-band">
        <p class="address">47 Brindle Court<br>Toronto, Ontario<br>M4K 2T8</p>
        <p class="phones">(647) 512-7730<span class="label">office</span><br>(647) 512-7731<span class="label">fax</span></p>
        <p class="email">selv@quendrix.example</p>
      </div>
      <p class="website">www.quendrix.example</p>
      <div class="brand">
        <span class="brand-dot"></span>
        <span class="brand-name">Quendrix</span>
      </div>
    </section>
  </div>
</body>
</html>
```